Domestic violence resource cards for distribution to at-risk patients in an emergency department

Using the attached image(or very similar) and text document, a tri-fold business card is requested that integrates the image on the outside and the document content throughout the card's remaining faces. A creative format is requested, one that does not look like the typical cold, uncaring bullet point outlines that are found in similar resource projects. Bold or larger font sizes are requested for headings and body text is not required to be aligned or justified and the bullet points in the supplied document can be removed for creative license. Palattes should be clear, avoiding neons or implied target gender. Legibility is paramount, but again a creative presentation of a very serious subject is our goal. These cards are intended to be distributed to patients or others in the emergency department that may benefit from domestic violence resources. The business card size is mandatory so that the card can be concealed if needed by the receiver.
Updates

Reason: There are several revisions from designers that we are anxiously awaiting; we want to provide time for these designers to submit new designs but also continue spending time with their families and friends around the holiday season.

Target Market(s)

Patients and family in contact with emergency services

Industry/Entity Type

Healthcare

Contact Information for Business Card

Double sided tri-fold card with image on outer sides, text content and resource phone numbers on the exterior. When complete, the card should fold to standard US business card size.

Font styles to use
Other font styles liked:
• Designer's choice, but clear and legible

Requirements
Must have
• See above description. Card must be tri-fold, fold down to standard business card size, remain easily readable, and fold along the long edge.
Should not have
• Cartoon images; bloated fonts or clipart; bright, flashy neon or rainbow-like colors; additional graphics or charts.

```html
<!DOCTYPE html>
<html lang="en">
<head>
<meta charset="utf-8">
<title>Break the Silence – Resource Card</title>
<link href="https://fonts.googleapis.com/css2?family=Roboto+Condensed:ital,wght@0,400;0,500;0,700;1,500&family=Montserrat:wght@800&display=swap" rel="stylesheet">
<style>
  :root{
    --stage:#e6c58f;
    --card:#000;
    --ink:#fff;
    --ink-dark:#111;
    --rule:#3a3a3a;
    --label:#3b2f22;
    --photo-dark:#151515;
    --photo-mid:#6d6d6d;
    --photo-light:#bdbdbd;
  }
  *{box-sizing:border-box;margin:0;padding:0}
  html,body{width:1200px;height:837px;overflow:hidden}
  body{background:var(--stage);position:relative;font-family:"Roboto Condensed",Arial,sans-serif;color:var(--ink)}

  .side-label{position:absolute;font-size:16px;color:var(--label);font-family:"Roboto Condensed",Arial,sans-serif}
  .side-label--insides{left:94px;top:414px}
  .side-label--back{left:1070px;top:447px}
  .side-label--front{left:1070px;top:655px}
  .bracket{position:absolute;left:128px;width:1px;background:var(--label)}
  .bracket--upper{top:68px;height:320px}
  .bracket--lower{top:448px;height:320px}

  .sheet{position:absolute;top:44px;width:424px;height:744px;display:flex;flex-direction:column}
  .sheet--inside{left:174px}
  .sheet--outside{left:614px}
  .panel{position:relative;height:248px;background:var(--card);border-bottom:1px solid var(--rule);overflow:hidden}
  .panel:last-child{border-bottom:0}

  .panel-title{position:absolute;left:0;top:15px;width:390px;height:22px;background:var(--ink);color:var(--ink-dark);
    font-weight:500;font-size:17px;line-height:22px;padding-left:42px}
  .panel-title--alt{padding-left:50px}

  .checklist{position:absolute;left:20px;top:48px;list-style:none}
  .checklist li{position:relative;padding-left:21px;font-size:11.2px;font-weight:500;height:19px;line-height:14px}
  .checklist li::before{content:"";position:absolute;left:0;top:1px;width:10px;height:12px;background:var(--ink)}
  .verdict{position:absolute;left:0;width:100%;top:221px;text-align:center;font-style:italic;font-weight:500;font-size:12px;padding-left:50px}

  .tips-head{position:absolute;left:0;top:17px;width:390px;height:50px;background:var(--ink);color:var(--ink-dark);padding:2px 0 0 20px}
  .tips-head strong{display:block;font-weight:500;font-size:20px;line-height:24px}
  .tips-head span{display:block;font-weight:500;font-size:16px;line-height:20px}

  .tips{position:absolute;left:20px;right:22px;list-style:none}
  .tips li{position:relative;padding-left:22px;font-size:10.6px;font-weight:500;line-height:13.5px;margin-bottom:7px}
  .tips li::before{content:"";position:absolute;left:0;top:1px;width:10px;height:12px;background:var(--ink)}
  .tips li.two-line::before{height:25px}
  .tips--plan{top:84px}
  .tips--more{top:12px}
  .tips--more li{margin-bottom:7.6px}

  .affirmations{position:absolute;left:36px;top:50px;list-style:none;width:300px}
  .affirmations li{position:relative;padding-left:25px;font-size:12px;font-weight:500;line-height:17px;margin-bottom:9.5px}
  .affirmations li::before{content:"";position:absolute;left:0;top:-1px;width:9px;height:20px;background:var(--ink)}
  .affirmations li.two-line::before{height:38px}
  .photo{position:absolute}
  .photo--hands{right:0;top:60px;width:100px;height:188px;
    background:radial-gradient(ellipse at 45% 40%,var(--photo-light) 0%,var(--photo-mid) 35%,var(--photo-dark) 75%,var(--card) 100%)}
  .photo--bound{left:0;top:0;width:262px;height:248px;
    background:radial-gradient(ellipse at 55% 55%,var(--photo-light) 0%,var(--photo-mid) 38%,var(--photo-dark) 72%,var(--card) 100%)}

  .directory{position:absolute;inset:0;transform:rotate(180deg);padding:32px 30px 0 30px}
  .directory-cols{display:flex;justify-content:space-between}
  .directory-col{display:flex;flex-direction:column;align-items:center;text-align:center}
  .contact{margin-bottom:16px}
  .contact-name{font-size:9.6px;line-height:11px}
  .contact-phone{font-size:16px;font-weight:700;line-height:17px;letter-spacing:.3px}
  .contact-note{font-size:9.6px;line-height:11px}
  .website{position:absolute;left:0;right:0;bottom:11px;text-align:center;font-size:11.5px;padding-left:100px}

  .slogan{position:absolute;left:271px;top:68px;font-family:"Montserrat",Arial,sans-serif;font-weight:800;font-size:31px;line-height:40px;color:var(--ink)}
</style>
</head>
<body>
  <span class="bracket bracket--upper"></span>
  <span class="side-label side-label--insides">Insides</span>
  <span class="bracket bracket--lower"></span>
  <span class="side-label side-label--back">Back</span>
  <span class="side-label side-label--front">front</span>

  <section class="sheet sheet--inside">
    <div class="panel">
      <h2 class="panel-title">Does Your Partner Ever...</h2>
      <ul class="checklist">
        <li>Hit, kick, push, choke or slap you?</li>
        <li>Intimidate you with weapons or harmful objects?</li>
        <li>Force you to engage in sexual acts?</li>
        <li>Threaten to hurt you, your children or your friends/family?</li>
        <li>Threaten to deport you or tell others your personal information?</li>
        <li>Control where you go, who you talk to or who you make friends with?</li>
        <li>Keep, hide or destroy your most important things?</li>
        <li>Blame, embarrass, or criticize you, make you feel worthless or guilty?</li>
        <li>Control your food, money, medicines or medical care?</li>
      </ul>
      <p class="verdict">You may be a victim of abuse or neglect!</p>
    </div>
    <div class="panel">
      <h2 class="tips-head"><strong>Leaving can be Tough and very Dangerous.</strong><span>Here are some tips to help you plan for safety:</span></h2>
      <ul class="tips tips--plan">
        <li class="two-line">Know people you can talk to and ask them to call the police if they hear a disturbance coming from your home</li>
        <li>Teach your children how to contact the police or fire department</li>
        <li>Practice how to get you and your children out of your home quickly and safely</li>
        <li class="two-line">Plan where you will go if you have to leave right away and know the location of local emergency shelters</li>
        <li class="two-line">Leave copies of important papers, keys, cash, IDs, and medicine with a friend or relative you trust</li>
      </ul>
    </div>
    <div class="panel">
      <ul class="tips tips--more">
        <li class="two-line">Have a small bag packed and ready at a friend or relative’s house so you can leave quick</li>
        <li class="two-line">Stay off social media or cancel you accounts so that you can’t be found online or through your friends</li>
        <li>Do not talk about your plans in public areas or in mixed groups</li>
        <li class="two-line">Open a credit card or bank account in your name only and do not use it until you are ready</li>
        <li class="two-line">Keep a chargedprepaid cell phone and a shelter hotline number ready for emergencies</li>
        <li>Review your plan often and only share with trusted friends or family</li>
        <li class="two-line">Be careful: you are at most risk during the first 72 hours after leaving an abusive situation</li>
        <li>Seek help at a police station, firehouse or hospital if needed</li>
      </ul>
    </div>
  </section>

  <section class="sheet sheet--outside">
    <div class="panel">
      <div class="photo photo--hands" role="img" aria-label="Black and white photo of one hand gripping another person's wrist"></div>
      <h2 class="panel-title panel-title--alt">Always Remember</h2>
      <ul class="affirmations">
        <li>You have a right to be safe anywhere</li>
        <li>You don’t deserve to be hit or threatened</li>
        <li>Your children deserve to grow up without violence</li>
        <li class="two-line">You have a right to protect you or your children until you are out of danger</li>
        <li>You are not alone</li>
        <li>You have choices</li>
      </ul>
    </div>
    <div class="panel">
      <div class="directory">
        <div class="directory-cols">
          <div class="directory-col">
            <div class="contact"><p class="contact-name">National Safe Homes Hotline</p><p class="contact-phone">1-800-555-0133</p></div>
            <div class="contact"><p class="contact-name">Crossroads Family Safety Resources</p><p class="contact-phone">303-555-0118</p></div>
            <div class="contact"><p class="contact-name">Oak Circle Violence Resources</p><p class="contact-phone">303-555-0152</p></div>
            <div class="contact"><p class="contact-name">The Harbor Center</p><p class="contact-phone">1-888-555-0172</p></div>
          </div>
          <div class="directory-col">
            <div class="contact"><p class="contact-name">Safe Harbor Metro:<br>Domestic Violence Crisis Resource</p><p class="contact-phone">303-555-0148</p></div>
            <div class="contact"><p class="contact-name">Open Bench:<br>Sexual Assault Victim’s Advocate</p><p class="contact-phone">303-555-0172</p></div>
            <div class="contact"><p class="contact-name">Respect First: Teen Dating Resource</p><p class="contact-phone">1-866-555-0194</p><p class="contact-note">or text “respect” to 40411</p></div>
          </div>
        </div>
        <p class="website">www.safehavenlist.org</p>
      </div>
    </div>
    <div class="panel">
      <div class="photo photo--bound" role="img" aria-label="Black and white photo of two clenched fists bound together with rope"></div>
      <h1 class="slogan">Break<br>the<br>Silence</h1>
    </div>
  </section>
</body>
</html>
```